Video Sharing Site

UPDATE 2: Thanks to everyone who has submitted so far. I have decided to include 2nd and 3rd prizes are well, and I believe with a robust price. If you chose to participate, I will be working with the 2nd and 3rd prize winners also to use your selected designs to complete the rest of the webpages as specified in the brief.

-

UPDATE 1: The key is attractive, SOPHISTICATED yet roomy.

You are free to use any software package you like ie. Joomla, Drupal, Wordpress etc. We just need access to the HTML/CSS.

-

Hello everyone.

We require the HTML/CSS for a video sharing website. Our website is called ClipHarborly.com. Think of a unique logo. However this is not the main focus. I will try to give you as much info about the website design as I can:

# Home page:
- with categories in sidebar
- video listings eg. popular, most viewed, etc.
- perhaps make promoted videos stand out

# simple login page

# User Profile page
- user details
- user uploaded videos
- profile comments

# User Profile Edit page

# User Profile Inbox page
- mock messages

# Search page
- list of videos that match search
- number of results
- pagination
- etc.

# Video page
- page where we are watching a video
- related videos
- video comments
- video description
- ratings (thumbs up/down)
- views
- tags
- etc.

# Video Categories page
- list of a few categories eg. newest, most viewed, highest rated, etc.
- with 10-15 videos under each

# Video Upload page with form

# About Us
- with subcategories in sidebar (different design to video categories in home page sidebar)

# Contact Us

# Header
- as any website an attractive search bar should accompany the header
- quick shortlinks to logged-in user eg. (5) comments, (3) inbox, logout, etc.

# Footer
- should be thick so that it can accommodate links to more specific (mock) web pages.

# General
- please be sure to include advertising
- Don't be afraid to use bold colors.
- I will not be selecting designs that are overly dark
- be sure that any page where video thumbnails are shown are accompanied by video rating, number of views and author.
- think about loading times as well. Avoid the use of large graphics where possible.

########### HINT ##########
The first two designs that I pick will be two different types:
- colorful
- quite conservative. Plenty of white with light greys
###########################

Thanks everybody who submits!

2nd and 3rd prized now included!

Just to keep you all updated. I have made a few changes to the brief. Mostly just to make it easier for you to gauge what I'm after.

I have received enough designs with blue in it. Please submit designs where blue is not a main color. Thank you all!

Industry/Entity Type

Software

Requirements
Must have
• A sophisticated layout. It must look like a professional video sharing website.

```html
<!DOCTYPE html>
<html lang="en">
<head>
<meta charset="utf-8">
<title>ClipHarborly — Registration</title>
<link href="https://fonts.googleapis.com/css2?family=Open+Sans:wght@400;600;700&display=swap" rel="stylesheet">
<style>
  :root {
    --page-bg: #e7e6e2;
    --brand-red: #d4173a;
    --brand-red-dark: #b60f2c;
    --brand-red-light: #e53b57;
    --ink: #333333;
    --ink-soft: #555555;
    --muted: #9a9a9a;
    --line: #d6d6d6;
    --field-top: #e4e4e4;
    --panel-bg: #ffffff;
    --nav-top: #f4f5f6;
    --nav-bottom: #d7dadd;
    --footer-bg: #333333;
    --footer-ink: #ffffff;
  }
  * { box-sizing: border-box; margin: 0; padding: 0; }
  html, body { width: 1029px; height: 1200px; overflow: hidden; }
  body {
    position: relative;
    background: var(--page-bg);
    font-family: "Open Sans", Arial, sans-serif;
    color: var(--ink);
    font-size: 12px;
  }
  a { color: inherit; text-decoration: none; }

  /* top utility links */
  .utility { position: absolute; top: 0; left: 0; width: 1029px; height: 27px; }
  .utility-public { position: absolute; left: 490px; top: 6px; font-size: 11px; white-space: nowrap; }
  .utility-account {
    position: absolute; left: 651px; top: 0; width: 292px; height: 27px;
    background: #dcdbd7; border-radius: 0 0 4px 4px;
    font-size: 11px; padding: 6px 0 0 12px; white-space: nowrap;
  }
  .sep { margin: 0 6px; }

  /* main shell */
  .shell {
    position: absolute; left: 85px; top: 37px; width: 859px; height: 1080px;
    background: var(--panel-bg);
    box-shadow: 0 0 6px rgba(0,0,0,.12);
    border-radius: 6px 6px 0 0;
  }
  .masthead {
    position: absolute; left: 0; top: 0; width: 859px; height: 104px;
    border-radius: 6px 6px 0 0;
    background: radial-gradient(ellipse at 30% 35%, var(--brand-red-light) 0%, var(--brand-red) 45%, var(--brand-red-dark) 100%);
  }
  .brand { position: absolute; left: 12px; top: 20px; display: flex; align-items: center; }
  .brand-dot { width: 62px; height: 62px; border-radius: 50%; background: #2a2a2a; margin-right: 32px; }
  .brand-name { font-size: 27px; font-weight: 400; color: #ffffff; letter-spacing: -.3px; line-height: 1; margin-top: -14px; }
  .brand-tag { position: absolute; left: 152px; top: 70px; font-size: 7px; line-height: 8px; color: #fff; letter-spacing: .3px; white-space: nowrap; }
  .upload-tab {
    position: absolute; left: 679px; top: 3px; width: 180px; height: 35px;
    background: var(--brand-red-dark); border-radius: 0 6px 0 4px;
    display: flex; align-items: center; padding-left: 16px; color: #fff; font-size: 19px;
  }
  .upload-tab svg { margin-right: 12px; }
  .search {
    position: absolute; left: 675px; top: 59px; width: 171px; height: 25px;
    background: #fff; border-radius: 3px; border: 1px solid #c9c9c9;
    font-size: 11px; color: #aaa; padding: 5px 0 0 10px;
  }
  .search svg { position: absolute; right: 6px; top: 4px; }

  .main-nav {
    position: absolute; left: 0; top: 104px; width: 859px; height: 43px;
    background: linear-gradient(var(--nav-top), var(--nav-bottom));
    border-bottom: 1px solid #c4c7ca; display: flex;
  }
  .main-nav a {
    height: 43px; display: flex; align-items: center; justify-content: center;
    font-size: 13px; font-weight: 600; color: #222; border-right: 1px solid #c4c7ca; white-space: nowrap;
  }

  .crumbs {
    position: absolute; left: 12px; top: 160px; width: 835px; height: 35px;
    background: linear-gradient(#f5f5f5, #e1e1e1); border: 1px solid #d2d2d2; border-radius: 5px;
    display: flex; align-items: center; font-size: 11px;
  }
  .crumbs .home { width: 50px; height: 33px; display: flex; align-items: center; justify-content: center; margin-right: 20px; }

  .panel {
    position: absolute; left: 12px; top: 208px; width: 835px; height: 827px;
    border: 1px solid #d2d2d2; border-radius: 5px; background: #fff;
  }
  .panel-head {
    height: 42px; background: linear-gradient(#fafafa, #e9e9e9); border-bottom: 1px solid #d6d6d6;
    border-radius: 5px 5px 0 0; padding: 11px 0 0 16px;
    color: var(--brand-red); font-weight: 700; font-size: 15px; letter-spacing: .3px;
  }
  .avatar {
    position: absolute; left: 38px; top: 82px; width: 96px; height: 86px;
    border: 3px solid #dcdcdc; background: #fff; padding: 6px;
  }
  .avatar-fill { width: 100%; height: 100%; background: linear-gradient(#f0f0f0, #c9cde3); }
  .btn-light {
    position: absolute; left: 149px; top: 113px; width: 106px; height: 23px;
    background: linear-gradient(#f7f7f7, #dedede); border: 1px solid #c8c8c8; border-radius: 3px;
    font-size: 11.5px; display: flex; align-items: center; justify-content: center;
  }

  .column { position: absolute; top: 194px; width: 335px; }
  .col-left { left: 38px; }
  .col-right { left: 419px; }
  .field { height: 53.3px; }
  .field label { display: block; font-size: 11.5px; line-height: 18px; }
  .req { color: var(--brand-red); margin-right: 3px; }
  .input {
    height: 22px; border: 1px solid var(--line); border-radius: 2px;
    background: linear-gradient(var(--field-top), #fff 55%);
  }
  .input.active { border-color: #e0768a; box-shadow: 0 0 3px rgba(212,23,58,.3); background: #fff; }
  .textarea { height: 118px; border: 1px solid var(--line); background: linear-gradient(#fff 40%, #e8e8e8); }
  .dob { display: flex; gap: 9px; }
  .dob .input { width: 78px; font-size: 11px; color: var(--muted); padding: 3px 0 0 5px; background: #fff; }
  .dob .select { position: relative; }
  .caret { position: absolute; right: 8px; top: 9px; width: 0; height: 0; border: 4px solid transparent; border-top: 5px solid #555; }
  .select-wide { position: relative; }

  .terms { position: absolute; left: 38px; top: 684px; display: flex; align-items: center; font-size: 11px; color: var(--ink-soft); }
  .checkbox { width: 12px; height: 12px; border: 1px solid #aaa; background: #f1f1f1; margin-right: 10px; }
  .btn-primary {
    position: absolute; left: 38px; top: 714px; width: 77px; height: 23px;
    background: linear-gradient(var(--brand-red-light), var(--brand-red-dark)); border-radius: 3px;
    color: #fff; font-size: 11px; font-weight: 700; display: flex; align-items: center; justify-content: center;
  }

  .site-footer {
    position: absolute; left: 0; top: 1117px; width: 1029px; height: 83px;
    background: var(--footer-bg); color: var(--footer-ink); text-align: center;
  }
  .footer-links { margin-top: 24px; font-size: 11px; }
  .footer-links .sep { margin: 0 6px; }
  .copyright { margin-top: 8px; font-size: 10px; }
  .copyright a { text-decoration: underline; }
</style>
</head>
<body>
  <div class="utility">
    <nav class="utility-public"><a href="#">Signup</a><span class="sep">|</span><a href="#">Help</a><span class="sep">|</span><a href="#">Browse</a></nav>
    <nav class="utility-account"><a href="#">My Account</a><span class="sep">|</span><a href="#">Inbox (2)</a><span class="sep">|</span><a href="#">Comments (3)</a><span class="sep">|</span><a href="#">Logout</a></nav>
  </div>

  <div class="shell">
    <header class="masthead">
      <div class="brand"><span class="brand-dot"></span><span class="brand-name">ClipHarborly</span></div>
      <div class="brand-tag">SHARE WITH THE WORLD</div>
      <a class="upload-tab" href="#">
        <svg width="34" height="24" viewBox="0 0 34 24"><path d="M9 22a8 8 0 0 1-1-16 10 10 0 0 1 19 2 7 7 0 0 1-1 14z" fill="#3a3a3a"/><path d="M17 8l-6 6h4v5h4v-5h4z" fill="#fff"/></svg>
        Upload
      </a>
      <div class="search">Search videos
        <svg width="16" height="16" viewBox="0 0 16 16"><circle cx="6.5" cy="6.5" r="4.8" fill="none" stroke="#aaa" stroke-width="2"/><path d="M10 10l5 5" stroke="#aaa" stroke-width="2.4"/></svg>
      </div>
    </header>

    <nav class="main-nav">
      <a href="#" style="width:82px">Home</a>
      <a href="#" style="width:86px">Videos</a>
      <a href="#" style="width:98px">About Us</a>
      <a href="#" style="width:153px">Become a Member</a>
      <a href="#" style="width:124px">Latest Videos</a>
      <a href="#" style="width:120px">Most Viewed</a>
      <a href="#" style="width:119px">Contact Info</a>
    </nav>

    <div class="crumbs">
      <span class="home"><svg width="18" height="16" viewBox="0 0 18 16"><path d="M9 1L1 8h2.5v7h4v-5h3v5h4V8H17z" fill="#555"/></svg></span>
      Register
    </div>

    <section class="panel">
      <h1 class="panel-head">REGISTRATION</h1>
      <div class="avatar"><div class="avatar-fill" role="img" aria-label="Default member avatar"></div></div>
      <a class="btn-light" href="#">Change Picture</a>

      <div class="column col-left">
        <div class="field"><label><span class="req">*</span>Username :</label><div class="input active"></div></div>
        <div class="field"><label><span class="req">*</span>Password :</label><div class="input"></div></div>
        <div class="field"><label><span class="req">*</span>Confirm Password :</label><div class="input"></div></div>
        <div class="field"><label><span class="req">*</span>Firstname :</label><div class="input"></div></div>
        <div class="field"><label><span class="req">*</span>Lastname :</label><div class="input"></div></div>
        <div class="field"><label><span class="req">*</span>Email :</label><div class="input"></div></div>
        <div class="field"><label>Describe Yourself :</label><div class="textarea"></div></div>
      </div>

      <div class="column col-right">
        <div class="field"><label>Date of Birth :</label>
          <div class="dob"><div class="input">Date</div><div class="input">Month</div><div class="input select">Year<span class="caret"></span></div></div>
        </div>
        <div class="field"><label>Mobile :</label><div class="input"></div></div>
        <div class="field"><label>Address :</label><div class="input"></div></div>
        <div class="field"><label>City :</label><div class="input"></div></div>
        <div class="field"><label>State/Province :</label><div class="input"></div></div>
        <div class="field"><label>Zip/Postalcode :</label><div class="input"></div></div>
        <div class="field"><label>Country :</label><div class="input select-wide"><span class="caret"></span></div></div>
      </div>

      <div class="terms"><span class="checkbox"></span>Hereby I have agreed the Terms &amp; Conditions</div>
      <a class="btn-primary" href="#">REGISTER</a>
    </section>
  </div>

  <footer class="site-footer">
    <nav class="footer-links"><a href="#">About us</a><span class="sep">|</span><a href="#">Contact us</a><span class="sep">|</span><a href="#">Terms</a><span class="sep">|</span><a href="#">Advertise</a><span class="sep">|</span><a href="#">Sitemap</a></nav>
    <p class="copyright">© 2011 <a href="#">ClipHarborly.com</a>. All rights reserved.</p>
  </footer>
</body>
</html>
```